Veltora Software Business Card Design

We are a new organization called Veltora. We are a software as a service provider. We deliver a project and program management solution via the internet, so everyone has the ability to work together and collaborate. Its an enterprise platform and we will focus on 50 plus employee company.

We have a website in place
www.veltora-demo.com

Use this as a start of producing the business card. The logo is there as well, but if you have a great and better solution...

Color scheme's could be inline with the website, but don't pin point on it. We can always change the website, logo, color scheme etc.

Target Market(s)

B2B, Projectmembers, projectmanagers, ICT, CTO, Marketing Managers

Industry/Entity Type

Software

Requirements
Must have
• Marten Kuyvelsma

Tel: +31 255 47 09 36
Mob: +31 6 927 15 062
marten@veltora-demo.com
Oostelingpad 84c
2184 KT Nieuw Vennep

Www.veltora-demo.com
social media links

```html
<!DOCTYPE html>
<html lang="en">
<head>
<meta charset="utf-8">
<title>Veltora Business Card</title>
<link rel="stylesheet" href="https://fonts.googleapis.com/css2?family=PT+Sans:ital,wght@0,400;0,700;1,700&display=swap">
<style>
  :root {
    --stage: #808080;
    --lime: #c2d92e;
    --ink: #1c1c1c;
    --stripe-grey: #4a4a4a;
    --paper: #ffffff;
    --text-dark: #1a1a1a;
    --shadow: rgba(0, 0, 0, 0.35);
  }
  * { margin: 0; padding: 0; box-sizing: border-box; }
  html, body {
    width: 1200px; height: 535px; overflow: hidden;
    background: var(--stage);
    font-family: "PT Sans", Arial, sans-serif;
  }
  .stage { position: relative; width: 1200px; height: 535px; }
  .card {
    position: absolute; overflow: hidden;
    box-shadow: 8px 8px 6px var(--shadow);
  }
  .card svg { display: block; }
  .card--front { left: 73px; top: 90px; width: 502px; height: 325px; }
  .card--back { left: 628px; top: 90px; width: 503px; height: 323px; }
  .side-label {
    position: absolute; top: 443px;
    color: var(--paper); font-weight: 700; font-size: 22px; letter-spacing: 0.5px;
  }
  .side-label--front { left: 90px; }
  .side-label--back { left: 630px; }
  .wordmark { font-family: "PT Sans", Arial, sans-serif; font-weight: 400; font-size: 50px; fill: var(--paper); }
  .contact-name { font-weight: 700; font-size: 21px; fill: var(--text-dark); }
  .contact-web, .contact-mail { font-weight: 700; font-style: italic; font-size: 13.5px; fill: var(--text-dark); }
  .contact-line { font-weight: 400; font-size: 10.5px; fill: var(--text-dark); }
</style>
</head>
<body>
<main class="stage">

  <section class="card card--front" aria-label="Card front">
    <svg width="502" height="325" viewBox="0 0 502 325">
      <defs>
        <pattern id="front-stripes" width="16" height="16" patternUnits="userSpaceOnUse">
          <rect width="16" height="16" fill="var(--lime)"/>
          <rect y="4" width="16" height="9" fill="var(--ink)"/>
        </pattern>
      </defs>
      <rect class="stripe-field" width="502" height="325" fill="url(#front-stripes)"/>
      <rect class="top-band" width="502" height="12" fill="var(--lime)"/>
      <rect class="bottom-band" y="305" width="502" height="20" fill="var(--lime)"/>
      <g class="hex-frame" fill="none" stroke="var(--lime)" stroke-width="34" stroke-linejoin="miter">
        <polygon points="10,165 85,35 235,35 310,165 235,295 85,295"/>
        <line x1="235" y1="35" x2="270" y2="-10"/>
        <line x1="85" y1="35" x2="55" y2="-10"/>
        <line x1="235" y1="295" x2="270" y2="340"/>
        <line x1="85" y1="295" x2="55" y2="340"/>
        <line x1="-10" y1="165" x2="10" y2="165"/>
      </g>
      <rect class="hex-core" x="40" y="60" width="240" height="210" fill="var(--lime)" opacity="0"/>
      <polygon class="hex-inner-line" points="30,165 97,52 223,52 290,165 223,278 97,278"
               fill="none" stroke="var(--paper)" stroke-width="2"/>
      <circle class="brand-dot" cx="160" cy="165" r="68" fill="none" stroke="var(--paper)" stroke-width="6"/>
      <text class="wordmark" x="288" y="183">Veltora</text>
    </svg>
  </section>

  <section class="card card--back" aria-label="Card back">
    <svg width="503" height="323" viewBox="0 0 503 323">
      <defs>
        <pattern id="back-stripes" width="12" height="12" patternUnits="userSpaceOnUse">
          <rect width="12" height="12" fill="var(--ink)"/>
          <rect y="5" width="12" height="3" fill="var(--stripe-grey)"/>
        </pattern>
      </defs>
      <rect class="stripe-field" width="503" height="323" fill="url(#back-stripes)"/>

      <g class="panels" fill="var(--paper)" stroke="var(--lime)" stroke-width="3">
        <polygon class="panel panel--name" points="-5,23 212,23 245,82 212,140 -5,140"/>
        <polygon class="panel panel--contact" points="-5,182 212,182 245,243 212,305 -5,305"/>
        <polygon class="panel panel--top" points="258,-5 424,-5 400,60 282,60"/>
        <polygon class="panel panel--bottom" points="282,268 400,268 424,330 258,330"/>
        <polygon class="panel panel--right-top" points="450,15 510,15 510,140 450,140 420,78"/>
        <polygon class="panel panel--right-bottom" points="450,185 510,185 510,310 450,310 420,248"/>
      </g>
      <g class="hex-frame" fill="none" stroke="var(--lime)">
        <polygon points="230,162 278,78 372,78 420,162 372,246 278,246" stroke-width="4"/>
        <polygon points="218,162 272,68 378,68 432,162 378,256 272,256" stroke-width="2"/>
      </g>

      <text class="contact-name" x="27" y="76">Marten Kuyvelsma</text>

      <g class="icon icon--globe" fill="none" stroke="#777" stroke-width="1">
        <circle cx="28" cy="98" r="8"/>
        <ellipse cx="28" cy="98" rx="3.5" ry="8"/>
        <line x1="20" y1="98" x2="36" y2="98"/>
      </g>
      <text class="contact-web" x="48" y="103">www.veltora-demo.com</text>

      <g class="icon icon--mail" fill="none" stroke="var(--text-dark)" stroke-width="1.3">
        <rect x="24" y="190" width="15" height="10"/>
        <polyline points="24,190 31.5,196 39,190"/>
      </g>
      <text class="contact-mail" x="50" y="200">marten@veltora-demo.com</text>

      <g class="icon icon--phone">
        <circle cx="31" cy="217" r="9" fill="none" stroke="var(--text-dark)" stroke-width="1.5"/>
        <path d="M27 211 q-2 6 3 11 q5 4 8 1 l-2 -3 -3 1 q-3 -2 -4 -5 l2 -2 z" fill="var(--text-dark)"/>
      </g>
      <text class="contact-line" x="50" y="214">Tel: +31 255 47 09 36</text>
      <text class="contact-line" x="50" y="229">Mob: +31 6 927 15 062</text>

      <path class="icon icon--pin" d="M31 270 C24 259 22 256 22 251 A9 9 0 0 1 40 251 C40 256 38 259 31 270 Z M31 248 a3 3 0 1 0 0.01 0 Z"
            fill="var(--text-dark)" fill-rule="evenodd"/>
      <text class="contact-line" x="50" y="253">Oostelingpad 84c</text>
      <text class="contact-line" x="50" y="267">2184 KT Nieuw Vennep</text>

      <g class="social-links" fill="var(--ink)">
        <rect x="56" y="280" width="20" height="20"/>
        <rect x="86" y="280" width="20" height="20"/>
        <rect x="116" y="280" width="20" height="20"/>
      </g>
    </svg>
  </section>

  <p class="side-label side-label--front">FRONT</p>
  <p class="side-label side-label--back">BACK</p>
</main>
</body>
</html>
```